Implant and Mini Implant trifold brochure.

Logo is attached. Our website: www.q7zdental.com

We need an Implant and Mini Implant Flyer (on the same flyer) to be done by someone experienced in Dental marketing.

To be mailed via : Whole Route Bulk Post-Retail® (WRBP Retail®)
You need to put a Retail Indica
Reference: https://www.kelvanpost.net/business/whole-route-bulk-post.htm
Whole Route Bulk Post-Retail Indicia Guidelines

Every WRBP mailpiece must have an WRBP indicia with “ECRWSS” in the address area, within the permit indicia, or below the permit, like the examples to the right.
The WRBP Retail Indicia does not have a specific size requirement but must be larger than .5" x .5".
The type font must be in all caps and at least a 4 point size.
Place the indicia in the upper right hand corner of the mailpiece.
It should fit in the area 1.625" from the right edge and 1.375" from top edge.
Leave 1/8" of space around the top and right edge.

There should be a picture of a senior citizen eating apple - that is what implants will provide.

One side English; Other side Spanish.

If you do not have idea on what implants and mini-implants are then please ask specific questions.

Make space for specials.

Target Market(s)

dental implants, dental mini implants

Font styles to use
Other font styles liked:
• leaving it open for designer.

Colors
00a990
33b8a4
87cfc6
cadf82

Requirements
Must have
• A senior citizen eating apple - that is what implants allow people to do.
• Once the design layout is finalized, we will provide text. I am leaving the design wide open. you may look at good templates for ideas, but please respect the copyright.
Nice to have
• Use implant and mini implant pictures.
• Images needed
• 1) 3 Easy Steps to Implant Restoration in 1 visit: Use three images: mouth with missing teeth; mouth with implant screws fitted; mouth with teeth restored.
• 2) Image for Implant based Denture.
• 3) Senior Citizen or a couple eating apple.
• Image must be of good quality; even if taken from different sources they must gel well with the over all design. The final design has to be stunning.
• Please do not provide me with designs that I can get from any printing company.
• The Text area:
• 1. Why Implants?
• 2. Space for implant based dentures.
• 3. Other spaces for filling in "Why visit Q7z Dental"
• Additional Info: Time to use the following text in the final output.
• Q7z Dental - Your home for Quartz-7-Zenith Dental care.
• Q7z Dental - Your Implant Destination.
• Why Implants?
• . Durable, long lasting teeth replacement
• . Surgically implanted metal posts or frames into the jawbone
• . Allows crowns, bridges or complete dentures to be placed on implants
• Why Implant Dentures?
• . Durable and Cost Effective
• . Your denture fabricated as normal denture
• . Four or more implants are placed in one visit
• . Your denture is then retrofitted to snap on the mini implant retention head
• . Stabilize your loose dentures in one visit
• Why Mini Implants?
• . Less involved procedure than conventional implants
• . Usually completed in one dental appointment
• . Replace missing teeth instantly
• Implants vs Mini-Implants
• Visit Q7z Dental for a complementary consultation to learn which option is best for you. Depending on various conditions including that of the jawbone, you may be recommended an implant or mini-implant based treatment.
• Implant or Mini-implant treatment may not be suitable for all patients. For implants to be successful, you need to have healthy gums and adequate bones to support the implants. You must also be willing to commit to proper maintenance of your implants or dentures. Visit your dentist at Q7z Dental to learn more.
• Spanish translation from google added below:
• Q7z Dental: su casa para atención Quartz-7-Zenith dental.
• Q7z Dental: su destino de implante.
• ¿Por qué los implantes?
• . Reemplazo duradero y duradero de los dientes
• . Puestos o marcos de metal implantados quirúrgicamente en la mandíbula
• . Permiten para colocan coronas, puentes o dentaduras completas en implantes
• ¿Por qué las dentaduras postizas?
• . Durable y rentable
• . Su dentadura fabricada como dentadura normal
• . Cuatro o más implantes se colocan en una visita
• . Su dentadura se reajusta para encajar en el cabezal de retención mini implante
• . Estabilice sus dentaduras sueltas en una visita
• ¿Por qué Mini Implantes?
• . Procedimiento menos complicado que los implantes convencionales
• . Generalmente se completa en una cita dental
• . Reemplace los dientes perdidos al
• Implantes vs Mini Implantes
• Visite Q7z Dental para obtener una consulta complementaria y conocer cuál es la mejor opción para usted. Dependiendo de varias condiciones, incluida de la mandíbula, se le puede recomenda un tratamiento basado en implantes o mini-implantes.
• El tratamiento con implantes o mini-implantes puede no ser adecuado para todos los pacientes. Para que los implantes tengan éxito, debe tener encías sanas y huesos adecuados para apoyar los implantes. También debe estar dispuesto a comprometerse con el mantenimiento adecuado de sus implantes o dentaduras postizas. Visite a su dentista en Q7z Dental para obtener más información.
Should not have
• blank spaces without purpose

```html
<!DOCTYPE html>
<html lang="en">
<head>
<meta charset="utf-8">
<title>Q7z Dental – Implants &amp; Mini Implants Trifold</title>
<link href="https://fonts.googleapis.com/css2?family=Montserrat:wght@600;700;800&family=Open+Sans:ital,wght@0,400;0,600;0,700;1,400&display=swap" rel="stylesheet">
<style>
:root{
  --teal:#00a990;
  --teal-mid:#33b8a4;
  --teal-light:#87cfc6;
  --teal-pale:#d9f0ec;
  --lime:#cadf82;
  --navy:#1f5fa8;
  --ink:#3b4a4a;
  --stage:#b9b9b9;
  --white:#ffffff;
}
*{box-sizing:border-box;margin:0;padding:0}
html,body{width:893px;height:1200px;overflow:hidden}
body{background:var(--stage);font-family:"Open Sans",Arial,sans-serif;color:var(--ink);position:relative}
.spread{position:absolute;left:20px;width:853px;height:560px;display:flex;background:var(--white);box-shadow:0 6px 18px rgba(0,0,0,.25)}
.spread--outside{top:30px}
.spread--inside{top:610px}
.panel{position:relative;width:284.33px;height:100%;overflow:hidden;border-right:1px solid #e4e4e4}
.panel:last-child{border-right:none}
.wave{position:absolute;left:0;top:0;width:100%;height:100%}
.photo{position:absolute}
.photo--circle{border-radius:50%;border:6px solid var(--teal);box-shadow:0 0 0 3px var(--white)}
.heading-pill{display:inline-block;background:var(--teal);color:var(--white);font-family:"Montserrat",Arial,sans-serif;font-weight:700;font-size:11px;padding:3px 14px 3px 10px;border-radius:0 12px 12px 0;margin:0 0 6px -14px}
.bullets{list-style:none;font-size:8.6px;line-height:1.45;margin-bottom:10px}
.bullets li{position:relative;padding-left:12px;margin-bottom:2px}
.bullets li::before{content:"";position:absolute;left:2px;top:5px;width:4px;height:4px;border-radius:50%;background:var(--teal)}
.copy{font-size:8.6px;line-height:1.45}
.brand{display:flex;align-items:center;gap:6px}
.brand__mark{width:26px;height:26px;border-radius:50%;background:var(--teal)}
.brand__name{font-family:"Open Sans",Arial,sans-serif;font-weight:700;font-size:20px;color:var(--teal);line-height:1}
.brand__tag{font-size:7px;letter-spacing:1.5px;color:var(--navy);margin-top:2px}
/* outside panel 1 */
.about{position:absolute;left:22px;right:18px;top:318px;color:var(--white)}
.about .copy{margin-bottom:14px}
.about .bullets{color:var(--white)}
.about .bullets li::before{background:var(--white)}
.about .heading-pill{background:var(--white);color:var(--teal)}
/* outside panel 2 */
.indicia{position:absolute;right:10px;top:10px;width:64px;height:60px;border:1px solid var(--ink);font-size:5.5px;font-weight:700;text-align:center;line-height:1.35;padding:6px 2px;background:var(--white)}
.addressee{position:absolute;left:22px;top:14px;width:150px;height:48px;border:1px dashed var(--ink);font-size:7px;padding:6px 8px;line-height:1.5;background:var(--white)}
.contact{position:absolute;left:28px;top:330px;right:20px}
.contact__list{list-style:none;margin-top:22px;font-size:10px;line-height:1.4}
.contact__list li{display:flex;gap:9px;align-items:flex-start;margin-bottom:12px}
.contact__list svg{flex:none;margin-top:2px}
/* outside panel 3 */
.cover-brand{position:absolute;left:26px;top:24px}
.cover-head{position:absolute;left:0;right:0;top:368px;text-align:center;font-family:"Montserrat",Arial,sans-serif;color:var(--ink)}
.cover-head__lead{font-size:16px;font-weight:700}
.cover-head__big{font-size:34px;font-weight:800;color:var(--navy);line-height:1.05;letter-spacing:.5px}
.cover-head__sub{font-size:15px;font-weight:700}
.info-pill{display:inline-block;margin-top:16px;background:var(--white);color:var(--navy);font-family:"Open Sans",Arial,sans-serif;font-size:8.5px;padding:4px 14px;border-radius:12px}
/* inside */
.inside-text{position:absolute;left:22px;right:18px;top:26px}
.es-block{position:absolute;left:22px;right:18px}
.photo-band{position:absolute;left:0;bottom:0;height:110px;background:linear-gradient(90deg,#1d2a2a,#4b5a55 45%,#23302f)}
</style>
</head>
<body>

<!-- OUTSIDE -->
<section class="spread spread--outside" aria-label="Brochure outside">
  <!-- Panel: about -->
  <div class="panel">
    <div class="photo" style="left:0;top:0;width:100%;height:250px;background:linear-gradient(120deg,#f5e6e0,#e9d2c8 55%,#f3efe9)" role="img" aria-label="Close-up of a smile beside a dental implant model"></div>
    <svg class="wave" viewBox="0 0 284 560" preserveAspectRatio="none" aria-hidden="true">
      <defs><linearGradient id="tealFade" x1="0" y1="0" x2="0" y2="1"><stop offset="0" stop-color="#87cfc6"/><stop offset="1" stop-color="#33b8a4"/></linearGradient></defs>
      <path d="M0 270 Q140 210 284 240 L284 560 L0 560Z" fill="url(#tealFade)"/>
      <path d="M0 268 Q140 208 284 238" fill="none" stroke="#00a990" stroke-width="4"/>
    </svg>
    <div class="photo photo--circle" style="left:70px;top:178px;width:120px;height:120px;background:linear-gradient(160deg,#c9a07e,#7a5238)" role="img" aria-label="Smiling child"></div>
    <div class="about">
      <p class="copy"><strong>“Q7z Dental”</strong> is “Quartz-7-Zenith Dental” - Your home for Quartz-7-Zenith dental care in Bellhaven and Cedar Ridge, Maryland. We accept most insurance plans. The friendly staff at Q7z Dental aims to provide individuals with a comfortable and relaxing environment where we strive to meet and exceed your expectations through professional results.</p>
      <span class="heading-pill">Why Implants?</span>
      <ul class="bullets">
        <li>Durable, long lasting teeth replacement</li>
        <li>Surgically implanted metal posts or frames into the jawbone</li>
        <li>Allows crowns, bridges or complete dentures to be placed on implants</li>
      </ul>
    </div>
  </div>

  <!-- Panel: mailing -->
  <div class="panel" style="background:linear-gradient(180deg,#6ec7bb 0%,#a9ddd5 45%,#ffffff 60%)">
    <div class="addressee">*********ECRWSS**<br>Postal Customer<br>City, State, Zip Code</div>
    <div class="indicia">PRSRT STD<br>ECRWSS<br>U.S. POSTAGE<br>PAID<br>WRBP RETAIL</div>
    <svg class="wave" viewBox="0 0 284 560" preserveAspectRatio="none" aria-hidden="true">
      <path d="M0 235 Q140 180 284 205" fill="none" stroke="#00a990" stroke-width="4"/>
    </svg>
    <div class="photo photo--circle" style="left:62px;top:140px;width:160px;height:160px;background:linear-gradient(150deg,#f0d9c8,#e6c1a8 55%,#bfe4dd)" role="img" aria-label="Patient smiling while a tooth shade guide is held up"></div>
    <div class="contact">
      <div class="brand"><span class="brand__mark"></span><div><div class="brand__name">Q7z Dental</div><div class="brand__tag">FAMILY DENTISTRY</div></div></div>
      <ul class="contact__list">
        <li><svg width="10" height="10" viewBox="0 0 24 24"><path d="M6.6 10.8a15 15 0 006.6 6.6l2.2-2.2a1 1 0 011-.25 11.4 11.4 0 003.6.6 1 1 0 011 1V20a1 1 0 01-1 1A17 17 0 013 4a1 1 0 011-1h3.5a1 1 0 011 1 11.4 11.4 0 00.6 3.6 1 1 0 01-.25 1z" fill="#3b4a4a"/></svg>555-014-2736</li>
        <li><svg width="10" height="10" viewBox="0 0 24 24"><circle cx="12" cy="12" r="10" fill="none" stroke="#3b4a4a" stroke-width="2"/><path d="M2 12h20M12 2c3 3 3 17 0 20M12 2c-3 3-3 17 0 20" fill="none" stroke="#3b4a4a" stroke-width="1.6"/></svg>www.q7zdental.com</li>
        <li><svg width="10" height="12" viewBox="0 0 24 28"><path d="M12 0a9 9 0 019 9c0 7-9 19-9 19S3 16 3 9a9 9 0 019-9z" fill="#3b4a4a"/><circle cx="12" cy="9" r="3.5" fill="#fff"/></svg>1180 Larkmoor Ave,<br>Bellhaven, MD 20911</li>
      </ul>
    </div>
  </div>

  <!-- Panel: cover -->
  <div class="panel">
    <svg class="wave" viewBox="0 0 284 560" preserveAspectRatio="none" aria-hidden="true">
      <path d="M0 70 Q140 40 284 60 L284 0 L0 0Z" fill="#ffffff"/>
      <path d="M0 300 Q150 270 284 300 L284 560 L0 560Z" fill="#87cfc6"/>
      <path d="M0 72 Q140 42 284 62" fill="none" stroke="#cadf82" stroke-width="5"/>
    </svg>
    <div class="cover-brand brand"><span class="brand__mark"></span><div><div class="brand__name">Q7z Dental</div><div class="brand__tag">FAMILY DENTISTRY</div></div></div>
    <div class="photo photo--circle" style="left:30px;top:100px;width:224px;height:224px;background:linear-gradient(140deg,#f2e6cf,#e7c9a8 50%,#d86e55)" role="img" aria-label="Senior couple sharing apples at home"></div>
    <div class="cover-head">
      <div class="cover-head__lead">Going to the Dentist</div>
      <div class="cover-head__big">CAN BE FUN</div>
      <div class="cover-head__sub">We Put Smile in your Life</div>
      <span class="info-pill">Additional Info: 06/08/2018</span>
    </div>
  </div>
</section>

<!-- INSIDE -->
<section class="spread spread--inside" aria-label="Brochure inside">
  <div class="photo-band" style="width:568px" role="img" aria-label="Dental technician polishing a denture with a handpiece"></div>

  <!-- Panel: English -->
  <div class="panel">
    <div class="inside-text">
      <span class="heading-pill">Why Implant Dentures?</span>
      <ul class="bullets">
        <li>Durable and Cost Effective</li>
        <li>Your denture fabricated as normal denture</li>
        <li>Four or more implants are placed in one visit</li>
        <li>Your denture is then retrofitted to snap on the mini implant retention head</li>
        <li>Stabilize your loose dentures in one visit</li>
      </ul>
      <span class="heading-pill">Why Mini Implants?</span>
      <ul class="bullets">
        <li>Less involved procedure than conventional implants</li>
        <li>Usually completed in one dental appointment</li>
        <li>Replace missing teeth instantly</li>
      </ul>
      <span class="heading-pill">Implants vs Mini-Implants</span>
      <ul class="bullets">
        <li>Visit Q7z Dental for a complementary consultation to learn which option is best for you. Depending on various conditions including that of the jawbone, you may be recommended an implant or mini-implant based treatment.</li>
        <li>Implant or Mini-implant treatment may not be suitable for all patients. For implants to be successful, you need to have healthy gums and adequate bones to support the implants. You must also be willing to commit to proper maintenance of your implants or dentures. Visit your dentist at Q7z Dental to learn more.</li>
      </ul>
    </div>
  </div>

  <!-- Panel: Spanish dentures -->
  <div class="panel">
    <div class="photo" style="left:0;top:0;width:100%;height:170px;background:linear-gradient(180deg,#f4f4f4,#e8e8e8)" role="img" aria-label="Rendered row of white teeth"></div>
    <svg class="wave" viewBox="0 0 284 560" preserveAspectRatio="none" aria-hidden="true">
      <path d="M0 40 Q60 10 140 0" fill="none" stroke="#cadf82" stroke-width="6"/>
      <path d="M0 48 Q60 18 150 0" fill="none" stroke="#33b8a4" stroke-width="3"/>
    </svg>
    <div class="photo photo--circle" style="left:62px;top:40px;width:150px;height:150px;background:linear-gradient(180deg,#ffffff 30%,#f3b8b8 65%,#e58b8b)" role="img" aria-label="Illustration of an implant post between two teeth in the gum"></div>
    <div class="es-block" style="top:222px">
      <span class="heading-pill">¿Por qué las dentaduras postizas?</span>
      <ul class="bullets">
        <li>Durable y rentable</li>
        <li>Su dentadura fabricada como dentadura normal</li>
        <li>Cuatro o más implantes se colocan en una visita</li>
        <li>Su dentadura se reajusta para encajar en el cabezal de retención del mini implante</li>
        <li>Estabilice sus dentaduras sueltas en una visita</li>
      </ul>
    </div>
    <div class="photo photo--circle" style="left:178px;top:340px;width:100px;height:100px;background:linear-gradient(180deg,#ffffff 30%,#f3b8b8 65%,#e58b8b)" role="img" aria-label="Illustration of an implant crown being seated"></div>
    <svg class="wave" viewBox="0 0 284 560" preserveAspectRatio="none" aria-hidden="true">
      <path d="M0 452 Q150 440 284 450" fill="none" stroke="#cadf82" stroke-width="3"/>
    </svg>
  </div>

  <!-- Panel: Spanish mini implants -->
  <div class="panel">
    <div class="photo" style="left:0;top:0;width:100%;height:230px;background:linear-gradient(180deg,#f1f1f1,#f6d3cc 70%,#eab0a6)" role="img" aria-label="Rendered implant screw beneath a row of teeth"></div>
    <svg class="wave" viewBox="0 0 284 560" preserveAspectRatio="none" aria-hidden="true">
      <path d="M0 240 Q150 200 284 215 L284 560 L0 560Z" fill="#87cfc6"/>
      <path d="M0 238 Q150 198 284 213" fill="none" stroke="#00a990" stroke-width="4"/>
      <path d="M0 548 L284 540" stroke="#cadf82" stroke-width="4"/>
    </svg>
    <div class="photo photo--circle" style="left:120px;top:90px;width:140px;height:140px;background:linear-gradient(150deg,#e9c8b2,#c98f73)" role="img" aria-label="Dentist checking tooth shade against a patient's teeth"></div>
    <div class="es-block" style="top:262px">
      <span class="heading-pill">¿Por qué Mini Implantes?</span>
      <ul class="bullets">
        <li>Procedimiento menos complicado que los implantes convencionales</li>
        <li>Generalmente se completa en una cita dental</li>
        <li>Reemplaza los dientes perdidos al instante</li>
      </ul>
      <span class="heading-pill">Implantes vs Mini Implantes</span>
      <ul class="bullets">
        <li>Visite Q7z Dental para obtener una consulta complementaria y conocer cuál es la mejor opción para usted. Dependiendo de varias condiciones, incluida de la mandíbula, se le puede recomendar un tratamiento basado en implantes o mini-implantes.</li>
        <li>El tratamiento con implantes o mini-implantes puede no ser adecuado para todos los pacientes. Para que los implantes tengan éxito, debe tener encías sanas y huesos adecuados. También debe estar dispuesto a comprometerse con el mantenimiento adecuado de sus implantes o dentaduras postizas. Visite a su dentista en Q7z Dental para obtener más información.</li>
      </ul>
    </div>
  </div>
</section>

</body>
</html>
```